Online Art Gallery & Art Management Firm looking for a business card

I'm launching an online art gallery (paintings, photography, drawings, furniture, books, ...) where people can buy all types of art. It's a platform where young and unknown artists can showcase their oeuvre.

Additionally, the venture will act as my advising company for artists. I help them out with their business side of life and become their representative.

The company name: The Velmora House
Logo is attached

I'm looking for something very classy and upmarket.
Updates

Reason: Logo wasn't finished yet...

The design should include the following information: - Name: Pieter Drovensky - Title: Founder - Mobile: +32 (0) 485 613 204 - E-mail: pieter@velmora-house.net - Website www.velmora-house.net I prefer the have the logo (without website) on the one side and the information on the other. Best regards Pieter

Target Market(s)

Art buyers / art dealers / artists / middle class / upmarket /

Industry/Entity Type

Artists

Colors

Designer to choose colors to be used in the design.

Requirements
Must have
• Must communicate credibility, trust and integrity
Nice to have
• Something classy, chique
Should not have
• Nothing to artistic or creative

```html
<!DOCTYPE html>
<html lang="en">
<head>
<meta charset="utf-8">
<title>The Velmora House – Business Card</title>
<link rel="stylesheet" href="https://fonts.googleapis.com/css2?family=Open+Sans:wght@300;400;600&family=Arimo:wght@400&display=swap">
<style>
  :root {
    --backdrop: #2b2433;
    --card-white: #ffffff;
    --card-black: #000000;
    --ink: #111111;
    --ink-soft: #333333;
    --ink-reverse: #f2f2f2;
  }
  * { margin: 0; padding: 0; box-sizing: border-box; }
  html, body {
    width: 1200px;
    height: 1000px;
    overflow: hidden;
    background: var(--backdrop);
  }
  .sheet {
    width: 1200px;
    height: 1000px;
    display: flex;
    flex-direction: column;
    align-items: center;
    justify-content: center;
    gap: 60px;
  }
  .card {
    width: 700px;
    height: 400px;
    background: var(--card-white);
    position: relative;
    overflow: hidden;
    box-shadow: 0 18px 40px rgba(0,0,0,0.35);
  }
  .wordmark {
    font-family: 'Open Sans', sans-serif;
    font-weight: 300;
    text-transform: uppercase;
    letter-spacing: 0.28em;
    white-space: nowrap;
  }

  /* Front: logo side */
  .card-front {
    display: flex;
    align-items: center;
    justify-content: center;
  }
  .card-front .wordmark {
    font-size: 40px;
    color: var(--ink);
  }

  /* Back: information side */
  .card-back__band {
    position: absolute;
    left: 0; top: 0;
    width: 100%;
    height: 170px;
    background: var(--card-black);
  }
  .card-back .wordmark {
    position: absolute;
    right: 40px;
    bottom: 238px;
    font-size: 28px;
    color: var(--ink-reverse);
  }
  .holder {
    position: absolute;
    left: 36px;
    top: 186px;
    font-family: 'Open Sans', sans-serif;
    text-align: center;
  }
  .holder__name {
    font-size: 25px;
    font-weight: 600;
    color: var(--ink);
    line-height: 1.15;
  }
  .holder__title {
    font-size: 16px;
    font-weight: 400;
    color: var(--ink-soft);
    margin-top: 2px;
  }
  .contacts {
    position: absolute;
    right: 36px;
    bottom: 34px;
    font-family: 'Arimo', sans-serif;
    font-size: 15px;
    line-height: 1.3;
    color: var(--ink);
  }
  .contacts__heading {
    text-align: center;
    text-transform: uppercase;
    font-size: 13px;
    letter-spacing: 0.04em;
  }
</style>
</head>
<body>
  <main class="sheet">
    <section class="card card-front" aria-label="Business card, logo side">
      <p class="wordmark">The Velmora House</p>
    </section>

    <section class="card card-back" aria-label="Business card, information side">
      <div class="card-back__band"></div>
      <p class="wordmark">The Velmora House</p>
      <div class="holder">
        <p class="holder__name">Pieter Drovensky</p>
        <p class="holder__title">Founder</p>
      </div>
      <div class="contacts">
        <p class="contacts__heading">Contacts</p>
        <p>Phone: +32 (0) 485 613 204</p>
        <p>E-mail: pieter@velmora-house.net</p>
        <p>Website: www.velmora-house.net</p>
      </div>
    </section>
  </main>
</body>
</html>
```